Visually Compelling Flyer Design - Harbor Perks

We are a life insurance company looking to create visually compelling flyers that gain attention of potential buyers and simplify the concept. It should be professional, friendly, approachable in nature. Our logo and several rough drafts are included.
We are looking to refine this look and make it ultra professional, clean and easy to follow. A creative brief with brand guidelines is also included.
FLYER 1 — PAY YOURSELF FIRST
EYEBROW TAG
YOUR COMPANY JUST UPGRADED YOUR BENEFITS
HEADLINE
One small decision. A lifetime of protection.
SUBHEADLINE
Permanent life insurance + long-term care coverage, starting at $1 a day.
EYEBROW TAG
CHOOSE YOUR DAILY INVESTMENT
STAT — TIER 1
$1 / day → $20,000 Life Insurance
STAT — TIER 2 (HERO — make this one biggest/most prominent)
$2 / day → $40,000 Life Insurance
★ Most Popular
STAT — TIER 3
$3 / day → $60,000 Life Insurance
CAPTION
Rate locked at enrollment. Benefit never decreases.
EYEBROW TAG
THREE BENEFITS. ONE POLICY.
SUBHEADLINE
Your money works three ways.
CALLOUT — BENEFIT 1
01 | Cash Value Growth
BODY
Averages 6% annually over the last 50 years — guaranteed never to fall below 3%. Better than any savings account. And if you ever need it, you can borrow against it. It's your money.
CALLOUT — BENEFIT 2
02 | Tax-Free Death Benefit
BODY
From day one, your family is protected. The full benefit is paid tax-free to the person you choose — no waiting period, no exceptions. That's your legacy, preserved.
CALLOUT — BENEFIT 3
03 | Long-Term Care Coverage
BODY
70% of Americans will need long-term care. This plan pays 75% of your benefit — upfront and tax-free — to cover those costs while you're still alive. Your retirement savings stay intact. Your family stays protected.
EYEBROW TAG
ALREADY HAVE LIFE INSURANCE THROUGH WORK?
SUBHEADLINE
That's term. It ends when you need it most.
BODY
Term life insurance is designed for temporary needs — protecting your paycheck, your mortgage, your kids while they're home. When you retire, the house is paid off and your children are grown. Term ends because the need ends.
BODY
But one need never ends: your final expenses and the cost of long-term care. This permanent plan stays with you after retirement — when term coverage is gone and getting new coverage is expensive or impossible.
COMPARISON — LEFT COLUMN HEADER
✕ TERM LIFE
COMPARISON — LEFT COLUMN ITEMS
Gets more expensive with age
Ends at retirement
No cash value
Temporary protection only
COMPARISON — RIGHT COLUMN HEADER
✓ THIS PLAN
COMPARISON — RIGHT COLUMN ITEMS
Rate locked forever at enrollment
Stays with you after retirement
Builds real cash value
Permanent protection for life
EYEBROW TAG
WHAT MAKES THIS DIFFERENT
SUBHEADLINE
Built for you. Stays with you.
CALLOUT
✓ Guaranteed Issued
No medical exams. No questions asked. You qualify.
CALLOUT
✓ Group Rate
Because you work here, you get pricing individuals can't access on their own.
CALLOUT
✓ Rate Locked Forever
Your premium never increases. Your benefit never decreases.
CALLOUT
✓ Portable
Change jobs. Retire. Your policy comes with you at the same rate.
CALLOUT
✓ Family Coverage
Protect your spouse and children under the same plan.
SUBHEADLINE
Protect retirement. Preserve dignity. Plan ahead.
CTA
Be on the lookout for your personalized coverage details.
CAPTION
Brokered by Harbor Perks · Underwritten by TrueLedger
FLYER 2 — THE LONG-TERM CARE REALITY
EYEBROW TAG
WHAT MOST PEOPLE DON'T KNOW — BUT SHOULD
HEADLINE
Most Americans are unprepared. You don't have to be.
SUBHEADLINE
The long-term care gap is real — and it affects families like yours.
EYEBROW TAG
THE NUMBERS ARE HARD TO IGNORE
STAT
70%
of Americans age 65 and older will need some form of long-term care during their lifetime.
CAPTION
Source: Pryce & Lomax, Review of Elder Welfare and Civic Planning, 2018
STAT
3–4%
of Americans over 50 own a private long-term care insurance policy. The gap between who needs it and who has it is staggering.
CAPTION
Source: Stroud & Bellamy, QVT Wellness Wire, 2023
STAT
$700 Billion+
Estimated annual U.S. long-term care cost — and it's growing every year.
CAPTION
Source: Delacroix Wynn & Pasternak, Civic Ledger Council, 2020
STAT
$470 Billion
The estimated value of unpaid care provided by family members every year. That's the real cost — measured in time, stress, and financial sacrifice.
CAPTION
Source: Tillman & Osei, Meridian Bureau
STAT
80%
of total long-term care spending goes directly to assist retirees. This isn't a young person's problem. But the time to plan is now.
CAPTION
SUBHEADLINE
Long-term care doesn't just cost money. It costs families.
BODY
When there's no plan in place, the people you love absorb the impact — financially, emotionally, and physically. Retirement savings built over a lifetime can disappear in months. Family members step back from their own lives to provide care. Dignity becomes a daily negotiation.
BODY
This is not inevitable. A small decision today changes the entire outcome.
EYEBROW TAG
THE SOLUTION
HEADLINE
The Pay Yourself First Principle.
BODY
Take the first $1, $2, or $3 you make every day and invest it in a permanent life insurance policy that includes long-term care coverage — underwritten by TrueLedger, offered through your employer at a group rate, and Guaranteed Issued for everyone.
STAT
$1 / day → $20,000 $2 / day → $40,000 $3 / day → $60,000
BODY
The benefit includes three protections in one: a cash value that grows at an average of 6% annually, a tax-free death benefit for your family, and long-term care coverage that pays 75% of your benefit upfront — tax-free — when you need care most.
SUBHEADLINE
Whether you're single, married, with children or without — there is protection in this plan for you.
HEADLINE
CTA
Look for your personalized offer. Coverage details are coming your way.
CAPTION
COPY RULES FOR DESIGNERS
Headlines are one idea only. Never more than two lines.
Stats stand alone. Never buried in a paragraph.
Body copy maxes at 3 sentences per block. If it's longer, cut it.
The $2/day tier is always the hero. Always.
"Guaranteed Issued" appears on both flyers. It's the most important trust signal.
TrueLedger is always attributed. Always.
The tagline is: Protect retirement. Preserve dignity. Plan ahead. — Use it verbatim.
Target Market(s)
Average Americans with a family - adults looking for life insurance
Industry/Entity Type
Life Insurance & Financial Retirement

```html
<!DOCTYPE html>
<html lang="en">
<head>
<meta charset="utf-8">
<title>Harbor Perks — Long-Term Care Flyer</title>
<link rel="stylesheet" href="https://fonts.googleapis.com/css2?family=Bebas+Neue&family=Lato:wght@400;700&display=swap">
<style>
  :root {
    --stage: #4a4a4a;
    --paper: #ffffff;
    --heading-blue: #0f3aa8;
    --navy: #062d8a;
    --deep-navy: #04256f;
    --teal: #1598c9;
    --pill-teal: #16a3d0;
    --body-grey: #555a62;
    --card-border: #2450b8;
    --white: #ffffff;
  }
  * { box-sizing: border-box; margin: 0; padding: 0; }
  html, body { width: 1200px; height: 791px; overflow: hidden; }
  body {
    background: var(--stage);
    font-family: "Lato", sans-serif;
    position: relative;
  }
  .flyer {
    position: absolute;
    top: 80px;
    width: 487px;
    height: 631px;
    background: var(--paper);
    overflow: hidden;
  }
  .flyer--reality { left: 79px; }
  .flyer--solution { left: 634px; }
  .abs { position: absolute; }
  .display { font-family: "Bebas Neue", sans-serif; font-weight: 400; letter-spacing: 0.2px; }
  .center { left: 0; right: 0; text-align: center; }

  /* Hero */
  .hero-photo {
    position: absolute; left: 0; top: 0; width: 487px; height: 275px;
    background:
      radial-gradient(ellipse 60% 45% at 55% 52%, #f6c36e 0%, rgba(240,160,80,0.6) 40%, rgba(0,0,0,0) 75%),
      linear-gradient(180deg, #6f5a52 0%, #b98766 28%, #e49c5c 46%, #c0794a 60%, #5e4232 82%, #3a2a24 100%);
  }
  .hero-shapes { position: absolute; left: 0; top: 0; }
  .brand {
    top: 12px; left: 191px; display: flex; align-items: center; gap: 8px;
  }
  .brand-mark {
    width: 44px; height: 44px; border-radius: 50%;
    border: 2px solid var(--white);
  }
  .brand-name {
    color: var(--white); font-family: "Lato", sans-serif; font-weight: 700;
    font-size: 13px; line-height: 14px; letter-spacing: 0.8px; text-transform: uppercase;
  }
  .eyebrow-pill {
    top: 97px; left: 150px; width: 187px; height: 26px; border-radius: 13px;
    background: var(--pill-teal); color: var(--white);
    font-size: 10px; line-height: 26px; text-align: center;
  }
  .hero-kicker { top: 130px; color: var(--white); font-size: 21px; line-height: 22px; }
  .hero-headline { top: 153px; color: var(--white); font-size: 44px; line-height: 44px; }
  .hero-sub { top: 199px; color: var(--white); font-size: 9px; line-height: 12px; }

  /* Stats */
  .section-title { color: var(--heading-blue); font-size: 25px; line-height: 26px; }
  .stats-title { top: 297px; }
  .stat-card {
    position: absolute; width: 140px; height: 130px;
    background: var(--paper);
    border: 1px solid var(--card-border);
    border-radius: 14px;
    overflow: hidden;
    box-shadow: 0 3px 10px rgba(20,60,160,0.12);
  }
  .stat-value {
    position: absolute; left: 17px; top: 15px;
    color: var(--heading-blue); font-size: 25px; line-height: 26px;
  }
  .stat-value sup { font-size: 10px; vertical-align: top; }
  .stat-desc {
    position: absolute; left: 17px; top: 45px; width: 114px;
    color: var(--body-grey); font-size: 7.2px; line-height: 12.2px;
  }
  .stat-source {
    position: absolute; left: 0; right: 0; bottom: 0; height: 29px;
    background: linear-gradient(90deg, #1a8fc6 0%, #0a45a8 100%);
    color: var(--white); font-size: 6.2px; line-height: 9.5px; text-align: center;
    display: flex; align-items: center; justify-content: center; padding: 0 10px;
  }
  .footer-shapes { position: absolute; left: 0; bottom: 0; }

  /* Solution flyer */
  .top-shapes { position: absolute; left: 0; top: 0; }
  .headline-blue { color: var(--heading-blue); font-size: 25px; line-height: 26px; }
  .body-copy {
    left: 48px; right: 48px; text-align: center;
    color: var(--body-grey); font-size: 8.7px; line-height: 14.7px;
  }
  .divider {
    left: 20px; width: 428px; top: 220px;
    border-top: 1px dotted #9aa6c8;
  }
  .tier {
    position: absolute; top: 333px; width: 91px; height: 49px;
    border: 1px solid var(--card-border); border-radius: 7px; text-align: center;
    background: var(--paper);
  }
  .tier-rate { display: block; margin-top: 9px; color: var(--heading-blue); font-size: 17px; line-height: 18px; }
  .tier-benefit { display: block; margin-top: 2px; color: var(--body-grey); font-size: 8.5px; line-height: 10px; }
  .closing-shapes { position: absolute; left: 0; top: 455px; }
  .closing-lead { top: 504px; color: var(--white); font-size: 9px; line-height: 13.5px; }
  .tagline { top: 541px; color: var(--white); font-size: 23px; line-height: 24px; }
  .cta { top: 565px; color: var(--white); font-size: 10.5px; line-height: 14px; font-weight: 700; }
  .attribution-pill {
    top: 588px; left: 97px; width: 293px; height: 28px; border-radius: 14px;
    background: var(--pill-teal); color: var(--white);
    font-size: 8.8px; line-height: 28px; text-align: center;
  }
</style>
</head>
<body>

<section class="flyer flyer--reality" aria-label="Flyer: The long-term care reality">
  <div class="hero-photo" role="img" aria-label="Photo: an older couple walking hand in hand along a palm-lined beach at sunset"></div>
  <svg class="hero-shapes" width="487" height="290" viewBox="0 0 487 290" aria-hidden="true">
    <defs>
      <linearGradient id="swooshBlue" x1="0" y1="0" x2="1" y2="0">
        <stop offset="0" stop-color="#1aa0d2"/>
        <stop offset="1" stop-color="#0a3fa6"/>
      </linearGradient>
    </defs>
    <path d="M0 195 Q243 321 487 205 V290 H0 Z" fill="#ffffff"/>
    <path d="M23 210 Q243 346 464 210 Q243 314 23 210 Z" fill="url(#swooshBlue)"/>
  </svg>

  <div class="abs brand">
    <span class="brand-mark"></span>
    <span class="brand-name">Harbor<br>Perks</span>
  </div>
  <div class="abs eyebrow-pill display">What most people don't know - but should</div>
  <h2 class="abs center hero-kicker display">Most Americans are unprepared.</h2>
  <h1 class="abs center hero-headline display">You don't have to be</h1>
  <p class="abs center hero-sub">The long-term care gap is real - and it affects families like yours.</p>

  <h2 class="abs center section-title stats-title display">The numbers are hard to ignore</h2>

  <svg class="footer-shapes" width="487" height="40" viewBox="0 0 487 40" aria-hidden="true">
    <path d="M40 40 Q243 -8 447 40 Z" fill="#0a3a9c"/>
    <path d="M40 40 Q243 -14 447 40 Q243 -4 40 40 Z" fill="url(#swooshBlue)"/>
  </svg>

  <article class="stat-card" style="left:22px; top:332px;">
    <div class="stat-value display">70%</div>
    <p class="stat-desc">of Americans age 65 and older will need some form of long-term care during their lifetime.</p>
    <p class="stat-source">Source: Pryce &amp; Lomax, Review of Elder Welfare and Civic Planning, 2018</p>
  </article>
  <article class="stat-card" style="left:174px; top:332px;">
    <div class="stat-value display">3–4%</div>
    <p class="stat-desc">of Americans over 50 own a private long-term care insurance policy. The gap between who needs it &amp; who has it is staggering</p>
    <p class="stat-source">Source: Stroud &amp; Bellamy, QVT Wellness Wire, 2023</p>
  </article>
  <article class="stat-card" style="left:326px; top:332px;">
    <div class="stat-value display">$700 Billion<sup>+</sup></div>
    <p class="stat-desc">Estimated annual U.S. long-term care cost — and it's growing every year.</p>
    <p class="stat-source">Source: Delacroix Wynn &amp; Pasternak, Civic Ledger Council, 2020</p>
  </article>
  <article class="stat-card" style="left:97px; top:476px;">
    <div class="stat-value display">$470 Billion</div>
    <p class="stat-desc">The estimated value of unpaid care provided by family members every year. That's the real cost - measured in time, stress</p>
    <p class="stat-source">Source: Tillman &amp; Osei, Meridian Bureau</p>
  </article>
  <article class="stat-card" style="left:249px; top:476px;">
    <div class="stat-value display">80%</div>
    <p class="stat-desc">of total long-term care spending goes directly to assist retirees. This isn't a young person's problem.</p>
    <p class="stat-source">Source: Tillman &amp; Osei, Meridian Bureau</p>
  </article>
</section>

<section class="flyer flyer--solution" aria-label="Flyer: The pay yourself first principle">
  <svg class="top-shapes" width="487" height="60" viewBox="0 0 487 60" aria-hidden="true">
    <defs>
      <linearGradient id="topBlue" x1="0" y1="0" x2="1" y2="0">
        <stop offset="0" stop-color="#1aa0d2"/>
        <stop offset="1" stop-color="#0a3fa6"/>
      </linearGradient>
    </defs>
    <path d="M26 0 Q243 88 460 0 Z" fill="#18a2cf"/>
    <path d="M36 3 Q243 92 449 6 Q243 70 36 3 Z" fill="url(#topBlue)"/>
  </svg>

  <h2 class="abs center headline-blue display" style="top:70px;">Long-term care doesn't just cost money.<br>It costs families.</h2>
  <p class="abs body-copy" style="top:124px;">When there's no plan in place, the people you love absorb the impact — financially, emotionally, and physically. Retirement savings built over a lifetime can disappear in months. Family members step back from their own lives to provide care. Dignity becomes a daily negotiation.</p>
  <p class="abs body-copy" style="top:183px;">This is not inevitable. A small decision today changes the entire outcome.</p>

  <div class="abs divider"></div>

  <h2 class="abs center headline-blue display" style="top:243px;">The Pay Yourself First Principle.</h2>
  <p class="abs body-copy" style="top:270px;">Take the first $1, $2, or $3 you make every day and invest it in a permanent life insurance policy that includes long-term care coverage — underwritten by TrueLedger, offered through your employer at a group rate, and Guaranteed Issued for everyone.</p>

  <div class="tier" style="left:93px;"><span class="tier-rate display">$1 / Day</span><span class="tier-benefit">$20,000</span></div>
  <div class="tier" style="left:198px;"><span class="tier-rate display">$2 / Day</span><span class="tier-benefit">$40,000</span></div>
  <div class="tier" style="left:303px;"><span class="tier-rate display">$3 / Day</span><span class="tier-benefit">$60,000</span></div>

  <p class="abs body-copy" style="top:398px;">The benefit includes three protections in one: a cash value that grows at an average of 6% annually, a tax-free death benefit for your family, and long-term care coverage that pays 75% of your benefit upfront — tax-free — when you need care most.</p>

  <svg class="closing-shapes" width="487" height="176" viewBox="0 0 487 176" aria-hidden="true">
    <defs>
      <linearGradient id="closingNavy" x1="0" y1="0" x2="0" y2="1">
        <stop offset="0" stop-color="#0a3a9e"/>
        <stop offset="1" stop-color="#04256f"/>
      </linearGradient>
      <linearGradient id="closingSwoosh" x1="0" y1="0" x2="1" y2="0">
        <stop offset="0" stop-color="#1aa0d2"/>
        <stop offset="1" stop-color="#0a3fa6"/>
      </linearGradient>
    </defs>
    <path d="M0 67 Q243 -26 487 67 V176 H0 Z" fill="url(#closingNavy)"/>
    <path d="M39 50 Q243 -32 449 50 Q243 -16 39 50 Z" fill="url(#closingSwoosh)"/>
  </svg>

  <p class="abs center closing-lead">Whether you're single, married, with children or without - there is<br>protection in this plan for you.</p>
  <h2 class="abs center tagline display">Protect retirement. Preserve dignity. Plan ahead.</h2>
  <p class="abs center cta">Look for your personalized offer. Coverage details are coming your way.</p>
  <div class="abs attribution-pill">Brokered by Harbor Perks · Underwritten by TrueLedger</div>
</section>

</body>
</html>
```